Design a shop front for a mortgage broker

Require to design the front and side of our new store. I would like our services to be listed:
* HOME LOANS
* INVESTMENT LOANS
* DEBT CONSOLIDATION
* COMMERCIAL LENDING
* VEHICLE FINANCE
* PROPERTY ADVICE
* FINANCIAL ADVICE
* INSURANCES

Our logo and the facade of the actual shop has been attached and I want to leave the colour scheme creativity to the designer. Please use the attached shop photos as a background for your designs.

The design will be applied as vinyl and can cover parts of the front of the window including part of the frame if required. But I would like clients to be able to see inside the store from parts of the middle window section.

On the door of the shop we require:

Opening Hours:
Monday - Friday: 09:00 - 18:00
Saturday: By Appointment Only
Sunday: Closed

Principle Broker: Oren Belsky
Mobile: 0427 903 218
Email: oren@lumacredit.com.au

I will need all of the high quality files in order to sent to the sign company to print on vinyl.

Please feel free to ask me any questions.

Industry/Entity Type

Mortgage Brokerage

Font styles to use
Sans Serif

Colors

Designer to choose colors to be used in the design.

Requirements
Must have
• Must have a list of our services.
• Must include the logo.
• Must include phone number 1800 07 LUMA / 1800 07 5862 (you can do a deviation of 5862 under the letters LUMA if you think it will be nice)
Nice to have
• Nice to have the 3 faded lights shining vertically from the bottom to the top similar to the banner I have uploaded.

```html
<!DOCTYPE html>
<html lang="en">
<head>
<meta charset="utf-8">
<title>Luma Credit – Shop Front Vinyl</title>
<link href="https://fonts.googleapis.com/css2?family=Roboto+Condensed:wght@400;700&family=Roboto:wght@500;700&display=swap" rel="stylesheet">
<style>
  :root {
    --backdrop: #7b7c7b;
    --paper: #ffffff;
    --brand-green: #0a8a4a;
    --deep-green: #04703a;
    --light-green: #15a35a;
    --gold-light: #f8f6a6;
    --gold-dark: #aaa63c;
    --ink-white: #ffffff;
  }
  * { box-sizing: border-box; margin: 0; padding: 0; }
  html, body {
    width: 1200px; height: 1200px; overflow: hidden;
    background: var(--backdrop);
  }
  .artboard { position: relative; width: 1200px; height: 1200px; }
  .panel {
    position: absolute; background: var(--paper); overflow: hidden;
    box-shadow: 10px 14px 22px rgba(0,0,0,0.35);
  }
  .panel svg.backdrop-art { position: absolute; inset: 0; }

  /* Front window panel */
  .front-panel { left: 88px; top: 222px; width: 582px; height: 698px; }
  .brand-name {
    position: absolute; left: 0; right: 0; top: 82px; text-align: center;
    font-family: "Roboto Condensed", sans-serif; font-weight: 700;
    font-size: 96px; letter-spacing: -1px; color: var(--brand-green);
    line-height: 1;
  }
  .web-address {
    position: absolute; left: 0; right: 0; top: 228px; text-align: center;
    font-family: "Roboto Condensed", sans-serif; font-weight: 400;
    font-size: 17px; color: var(--brand-green);
  }
  .service-list {
    position: absolute; left: 0; width: 592px; top: 454px; list-style: none;
    text-align: center;
    font-family: "Roboto Condensed", sans-serif; font-weight: 400;
    font-size: 23px; line-height: 27.2px; color: var(--ink-white);
  }

  /* Door panel */
  .door-panel { left: 710px; top: 222px; width: 383px; height: 836px; }
  .hours-box {
    position: absolute; left: 84px; top: 68px; width: 241px; height: 149px;
    background: var(--brand-green); border-radius: 14px;
    display: flex; flex-direction: column; justify-content: center; align-items: center;
    font-family: "Roboto", sans-serif; font-weight: 700; font-size: 13px;
    line-height: 17.5px; color: var(--ink-white); text-align: center;
  }
  .contact-frame { position: absolute; left: 0; top: 0; }
  .broker-contact {
    position: absolute; left: 60px; width: 245px; top: 234px; text-align: center;
    font-family: "Roboto", sans-serif; font-weight: 700; font-size: 12.8px;
    line-height: 16.5px; color: var(--brand-green);
  }
</style>
</head>
<body>
<main class="artboard">

  <section class="panel front-panel">
    <svg class="backdrop-art" width="582" height="698" viewBox="0 0 582 698">
      <defs>
        <linearGradient id="goldSweep" x1="0" y1="0" x2="1" y2="0">
          <stop offset="0" stop-color="#ffffff"/>
          <stop offset="0.15" stop-color="var(--gold-dark)"/>
          <stop offset="0.6" stop-color="var(--gold-light)"/>
          <stop offset="1" stop-color="var(--gold-dark)"/>
        </linearGradient>
        <linearGradient id="greenTowers" x1="0" y1="0" x2="1" y2="1">
          <stop offset="0" stop-color="var(--deep-green)"/>
          <stop offset="0.5" stop-color="var(--brand-green)"/>
          <stop offset="1" stop-color="var(--light-green)"/>
        </linearGradient>
      </defs>
      <path d="M0,418 Q300,182 582,330 L582,698 L0,698Z" fill="url(#goldSweep)"/>
      <path d="M0,426 Q300,238 582,386 L582,698 L0,698Z" fill="url(#greenTowers)"
            role="img" aria-label="Green-tinted photo of office towers seen from below"/>
    </svg>
    <h1 class="brand-name">Luma Credit</h1>
    <p class="web-address">www.lumacredit.com.au</p>
    <ul class="service-list">
      <li>HOME LOANS</li>
      <li>INVESTMENT LOANS</li>
      <li>DEBT CONSOLIDATION</li>
      <li>COMMERCIAL LENDING</li>
      <li>VEHICLE FINANCE</li>
      <li>PROPERTY ADVICE</li>
      <li>FINANCIAL ADVICE</li>
      <li>INSURANCES</li>
    </ul>
  </section>

  <section class="panel door-panel">
    <svg class="backdrop-art" width="383" height="836" viewBox="0 0 383 836">
      <defs>
        <linearGradient id="doorGold" x1="0" y1="0" x2="1" y2="0">
          <stop offset="0" stop-color="var(--gold-dark)"/>
          <stop offset="0.65" stop-color="var(--gold-light)"/>
          <stop offset="1" stop-color="var(--gold-light)"/>
        </linearGradient>
        <linearGradient id="doorGreen" x1="0" y1="1" x2="1" y2="0">
          <stop offset="0" stop-color="var(--deep-green)"/>
          <stop offset="1" stop-color="var(--brand-green)"/>
        </linearGradient>
      </defs>
      <path d="M0,682 Q250,570 383,600 L383,836 L0,836Z" fill="url(#doorGold)"/>
      <path d="M0,706 Q250,620 383,646 L383,836 L0,836Z" fill="url(#doorGreen)"
            role="img" aria-label="Green-tinted photo of glass office towers"/>
    </svg>
    <svg class="contact-frame" width="383" height="320" viewBox="0 0 383 320">
      <path d="M76,110 L68,110 Q58,110 58,120 L58,292 Q58,302 68,302 L296,302 Q306,302 306,292 L306,226"
            fill="none" stroke="var(--brand-green)" stroke-width="2.5"/>
    </svg>
    <div class="hours-box">
      <p>Opening Hours:</p>
      <p>Monday - Friday: 09:00 - 18:00</p>
      <p>Saturday: By Appointment Only</p>
      <p>Sunday: Closed</p>
    </div>
    <div class="broker-contact">
      <p>Principle Broker: Oren Belsky</p>
      <p>Mobile: 0427 903 218</p>
      <p>Email: oren@lumacredit.com.au</p>
    </div>
  </section>

</main>
</body>
</html>
```